Business Card Design Project

We need a business card for our IT services provider business. We provide services to small and medium business, and would like something that reflects the color scheme / branding on our recently updated website - www.tallobrix.com.au

The card type we have chosen is a matte laminated double sided configuration at 86mm x 54mm on 350 GSM cardboard.
Updates

Target Market(s)

Small and Medium Business owners

Industry/Entity Type

Business

Requirements
Must have
• *Details on all cards*

Company Name: Tallobrix Pty Ltd
ABN: 52 683 914 207
Address: 47-49 Pembury Street, Ashcombe Vale, Victoria 3172
Phone: 1300 GRAB UP
Fax: 03 9417 6258
Website: www.tallobrix.com.au
Logo/Handprint Icon

*Person Specific*

```html
<!DOCTYPE html>
<html lang="en">
<head>
<meta charset="utf-8">
<title>Tallobrix Pty Ltd – Business Card</title>
<link rel="stylesheet" href="https://fonts.googleapis.com/css2?family=Macondo&display=swap">
<style>
  :root {
    --stage-light: #c4c4c4;
    --stage-mid: #737170;
    --stage-dark: #2a2624;
    --stage-frame: #4a4a4a;
    --card-front: #1b3f54;
    --card-back: #b8d9de;
    --card-edge: #2b2b2b;
    --brand-accent: #2f6ea6;
    --ink-light: #ffffff;
    --ink-dark: #2c4a5a;
  }
  * { box-sizing: border-box; margin: 0; padding: 0; }
  html, body {
    width: 1200px;
    height: 1194px;
    overflow: hidden;
  }
  body {
    position: relative;
    font-family: "Macondo", fantasy;
    background: linear-gradient(35deg, var(--stage-light) 0%, var(--stage-mid) 50%, var(--stage-dark) 100%);
    border: 2px solid var(--stage-frame);
  }
  .card {
    position: absolute;
    border: 1.5px solid var(--card-edge);
    border-radius: 54px;
  }
  .card--front {
    left: 54px;
    top: 74px;
    width: 507px;
    height: 806px;
    background: var(--card-front);
  }
  .card--back {
    left: 602px;
    top: 338px;
    width: 505px;
    height: 804px;
    background: var(--card-back);
  }
  .brand-name {
    position: absolute;
    left: 0;
    right: 0;
    top: 176px;
    text-align: center;
    font-size: 116px;
    line-height: 1;
    color: var(--ink-light);
  }
  .brand-mark {
    position: absolute;
    left: 150px;
    top: 300px;
    width: 280px;
    height: 280px;
    border-radius: 50%;
    background: var(--brand-accent);
  }
  .company-name {
    position: absolute;
    left: 18px;
    top: 382px;
    font-size: 64px;
    font-weight: 400;
    line-height: 1;
    color: var(--ink-dark);
    white-space: nowrap;
  }
  .contact-list {
    position: absolute;
    left: 44px;
    top: 494px;
    list-style: none;
    font-size: 25.5px;
    line-height: 39.5px;
    color: var(--ink-dark);
    white-space: nowrap;
  }
  .contact-list .indent { padding-left: 82px; }
  .contact-list .flush { margin-left: 3px; }
</style>
</head>
<body>
  <section class="card card--front" aria-label="Card front">
    <p class="brand-name">Tallobrix</p>
    <div class="brand-mark" role="img" aria-label="Brand mark area"></div>
  </section>

  <section class="card card--back" aria-label="Card back">
    <h1 class="company-name">Tallobrix pty ltd</h1>
    <ul class="contact-list">
      <li>ABN: 52 683 914 207</li>
      <li>Address: 47-49 Pembury Street,</li>
      <li class="indent">Ashcombe Vale,</li>
      <li class="indent">Victoria 3172</li>
      <li class="flush">Phone: 1300 GRAB UP</li>
      <li class="flush">Fax: 03 9417 6258</li>
      <li class="flush">Website: www.tallobrix.com.au</li>
    </ul>
  </section>
</body>
</html>
```